We need a tri-fold brochure design.

We need a tri-fold brochure design to highlight our Lanternwood Seed Program. The brochure we have now is functional, but we would like a design that is eye catching. We have a sample brochure that we have attached with the wording we would like to include for the brochure. We would like something that will catch a potential donor’s eye.
Updates

The tri-fold brochure should be in the same order as the sample brochure that was attached. The descriptions align with the photos. We would like to use the same cover shot that is on the sample photo. Thank you. Added Saturday, March 28, 2015

Target Market(s)

This brochure will be given out to potential donors.

Colors
3176b5

Requirements
Must have
• It must be eye catching.
Nice to have
• We would like to have something that will be engaging and make people want to give to our agency.
Should not have
• We don't want the kiddie text.

```html
<!DOCTYPE html>
<html lang="en">
<head>
<meta charset="utf-8">
<title>Lanternwood Seed Program – Brochure Inside Spread</title>
<link href="https://fonts.googleapis.com/css2?family=Questrial&display=swap" rel="stylesheet">
<style>
  :root {
    --brand-blue: #3176b5;
    --paper: #ffffff;
    --backdrop: #e8e5e0;
    --text-light: #ffffff;
    --fold-line: rgba(0, 0, 0, 0.08);
  }
  * { box-sizing: border-box; margin: 0; padding: 0; }
  html, body {
    width: 1200px;
    height: 876px;
    overflow: hidden;
    background: var(--backdrop);
  }
  .spread {
    position: absolute;
    left: 60px;
    top: 58px;
    width: 1080px;
    height: 760px;
    background: var(--paper);
    display: grid;
    grid-template-columns: repeat(3, 1fr);
    grid-template-rows: 175px 225px 180px 180px;
    box-shadow: 0 6px 18px rgba(0, 0, 0, 0.18);
  }
  .panel-photo {
    width: 100%;
    height: 100%;
  }
  .photo-science    { background: linear-gradient(160deg, #c9b59a 0%, #8d6f5b 55%, #3b3441 100%); }
  .photo-reading    { background: linear-gradient(160deg, #2a2530 0%, #6b5a63 50%, #b9a6a0 100%); }
  .photo-stem       { background: linear-gradient(160deg, #e4ded2 0%, #b6a08e 50%, #4b67a0 100%); }
  .photo-firstgrade { background: linear-gradient(160deg, #ecebe6 0%, #a7a4a0 50%, #5b6a85 100%); }
  .photo-weather    { background: linear-gradient(160deg, #cfc8c2 0%, #8e6f67 50%, #3c3a4e 100%); }
  .photo-music      { background: linear-gradient(160deg, #8a7865 0%, #6e4a3a 50%, #c7a79a 100%); }

  .panel-copy {
    background: var(--brand-blue);
    color: var(--text-light);
    font-family: "Questrial", "Century Gothic", sans-serif;
    font-size: 13px;
    line-height: 1.38;
    padding: 22px 32px 14px;
    display: flex;
    align-items: flex-start;
    overflow: hidden;
  }
  .panel-copy.row-bottom { padding-top: 28px; }

  .fold {
    position: absolute;
    top: 0;
    width: 1px;
    height: 100%;
    background: var(--fold-line);
  }
  .fold-left  { left: 360px; }
  .fold-right { left: 720px; }
</style>
</head>
<body>
  <main class="spread">
    <div class="panel-photo photo-science" role="img" aria-label="Group photo of junior high science students and teachers holding grant award checks in a classroom"></div>
    <div class="panel-photo photo-reading" role="img" aria-label="Group photo of elementary students and teacher holding grant award checks in a decorated reading classroom"></div>
    <div class="panel-photo photo-stem" role="img" aria-label="Group photo of elementary students, teacher and foundation members holding grant award checks under a classroom banner"></div>

    <p class="panel-copy row-top">Marisol Vantreel, along with Dorian Hatchell, at Crestmoor Junior High received two grants totaling $2,653. These grants enabled both teachers to give their junior high science students a better understanding of chemistry and physics as well as a deeper understanding of the earth through hands-on activities and equipment.</p>
    <p class="panel-copy row-top">Helena Strand, Willowgate Elementary, was awarded four grants totaling $2,885. Three of these grants are designed to improve reading levels, interest in reading, and passion for reading in elementary students by increasing the availability of Leveled Reader books, Meadowlist books, and audio books. The fourth grant provides supplies and materials to reintroduce Fine Arts at the elementary level through art and drama.</p>
    <p class="panel-copy row-top">Tessa Varnum, Pinecrest Elementary, was awarded three grants totaling $981. Two of these grants provide books to help increase reading proficiency, enthusiasm about reading, and provide essential knowledge of scientific concepts as well as reinforce the importance of STEM (science, technology, engineering, and math) in a creative way. The third grant provides supplies and materials for the newly-formed elementary art club.</p>

    <div class="panel-photo photo-firstgrade" role="img" aria-label="Group photo of first grade students, parents and teacher gathered in a classroom with a grant award check"></div>
    <div class="panel-photo photo-weather" role="img" aria-label="Group photo of elementary students and teacher holding grant award checks and program signs"></div>
    <div class="panel-photo photo-music" role="img" aria-label="Group photo of junior high orchestra students holding violins, cellos and a grant award check"></div>

    <p class="panel-copy row-bottom">Nora Kessling, Harborview Elementary, received one grant for $2,348. Books purchased through this grant will help her first grade students to become successful readers by challenging them to read more books and increase their reading level at this important stage in their education.</p>
    <p class="panel-copy row-bottom">Rafael Quintero, Tidewater Elementary, received two grants totaling $715. These grants involve giving elementary students a better understanding of the sun and its properties and learning weather forecasting abilities.</p>
    <p class="panel-copy row-bottom">Adriana Sollis-Brandt, Harborview Junior High received a $1,000 grant to help implement technology into the musical classroom. This grant includes a tablet and a number of applications to assist junior high students in creating their own music and tuning their instruments.</p>

    <span class="fold fold-left" aria-hidden="true"></span>
    <span class="fold fold-right" aria-hidden="true"></span>
  </main>
</body>
</html>
```